Hair and Grooming Salon Flyer

I need a double sided flyer to promote 2 services provided by 2 individual professionals in our salon (one offer per side?)

1. A MALE "POWER HOUR" (75mins of serious grooming) with Brenna
Choose any 2 male treatments from the following menus for just $99!
BODY
-30 minute deep tissue massage
-full body detox body scrub
-Mens maintenance pedicure
-Mens maintenance manicure
FACE
- Express Deep Cleanse Facial
- Microdermabrasion
- 30 minute Indian head massage
MANSCAPING
-Back and shoulder wax
-Chest and Stomach
-Mens Basic bikini (speedo line)
-1/2 leg wax

2. MARLOWS "COLOUR BAR" (available Tues - Thurs) $99
Freshen up your look in the experienced hands of a Senior Stylist
1/2 head of foils or regrowth colour
Precision style cut and Blowdry
Appointments after 4pm - enjoy a complimentry glass of wine

The design should communicate experience and confidence with a sense of specialty
Our colours are black white silver grey with bright orange accents

Terms & conditions
Offer 1. Offered by appointment with Brenna our Male grooming therapist only various days and times subject to availability, subject to change without notice; limitless services per customer

Offer 2. Available for limited times - Sept 16 - Nov 6 2014; Dec 30-Feb 27 with Marlow only and for one service per customer at advertised price of $99
Updates

Project Deadline Extended
Reason: One of my photos was not uploaded correctly and two photos of the same person was (to give choice) therefore the design for COLOUR BAR is incorrect. The photograph of the woman with short blonde hair is the hairdresser I wish to feature in the flyer for the COLOUR BAR My apologies

Target Market(s)

New clients! offer 1 - men, professionals / offer 2 - young adult women funky hair

Industry/Entity Type

Salon

Requirements
Must have
• Must have one offer per side of flyer
Must have photo shots of Brenna (2 provided, the second and third, you choose which is best) and of Marlow (first photo short blonde hair)
We have an extremely localised and personalised business but we need more clients for colour work so this is an introductory offer for hairdressing
and more male clients for Brenna who had an inner city practice with a large male clientele this will be an ongoing package on our menu

www.velquorastudio.net.au for look and feel of salon
and contact details
Should not have
• dont want to appear cheap or discounted - just packaged intelligently

```html
<!DOCTYPE html>
<html lang="en">
<head>
<meta charset="utf-8">
<title>Velquora Salon Flyer</title>
<link rel="stylesheet" href="https://fonts.googleapis.com/css2?family=Lato:ital,wght@0,400;0,700;0,900;1,400&family=Lora:ital,wght@1,400&display=swap">
<style>
  :root {
    --orange: #f47c30;
    --black: #111111;
    --ink: #1c1c1c;
    --grey: #9a9a9a;
    --silver: #d8d8d8;
    --page: #ffffff;
    --backdrop: #efefef;
  }
  * { box-sizing: border-box; margin: 0; padding: 0; }
  html, body { width: 1200px; height: 900px; overflow: hidden; }
  body { background: var(--backdrop); font-family: "Lato", sans-serif; color: var(--ink); position: relative; }

  .flyer-side { position: absolute; top: 120px; width: 470px; height: 660px; background: var(--page); box-shadow: 0 4px 14px rgba(0,0,0,.18); overflow: hidden; }
  .side-men { left: 80px; }
  .side-colour { left: 650px; }
  .abs { position: absolute; }

  .brand-name { font-family: "Lato", sans-serif; font-weight: 400; font-size: 40px; color: var(--black); letter-spacing: .5px; line-height: 1; }
  .brand-tagline { font-size: 10px; font-weight: 400; color: #333; letter-spacing: 1.2px; }
  .intro { font-size: 10.5px; font-weight: 700; line-height: 17px; }

  /* Power hour band */
  .power-band { left: 0; top: 143px; width: 470px; height: 62px; background: var(--black); }
  .power-box { left: 6px; top: 5px; width: 385px; height: 52px; background: var(--orange); }
  .power-title { left: 33px; top: 8px; font-size: 16px; font-weight: 900; color: var(--black); line-height: 20px; white-space: nowrap; }
  .power-sub { left: 234px; top: 4px; font-size: 9.5px; font-weight: 700; color: var(--black); text-align: center; line-height: 14px; white-space: nowrap; }
  .power-sub strong { font-size: 11px; }
  .power-line { left: 0; width: 385px; top: 35px; text-align: center; font-size: 10px; font-weight: 700; color: var(--black); line-height: 13px; white-space: nowrap; }
  .power-photo { left: 396px; top: 4px; width: 56px; height: 54px; background: linear-gradient(135deg,#3a3a3a,#8b7b70); }

  .photo-frame { border: 2px solid var(--orange); border-radius: 9px; overflow: hidden; background: #fff; padding: 3px; }
  .photo-fill { width: 100%; height: 100%; border-radius: 6px; }

  .section-label { background: var(--orange); color: var(--black); font-weight: 900; font-size: 12px; padding: 1px 5px; line-height: 16px; }
  .menu-list { list-style: none; font-size: 10.5px; font-weight: 700; line-height: 17px; white-space: nowrap; }
  .align-right { text-align: right; }

  .offer-tag { left: 40px; top: 240px; width: 95px; height: 52px; }
  .offer-tag .tag-back { left: 4px; top: 5px; width: 92px; height: 50px; background: var(--silver); transform: rotate(-4deg); }
  .offer-tag .tag-front { left: 0; top: 0; width: 90px; height: 48px; background: var(--orange); box-shadow: 3px 3px 0 #333; display: flex; align-items: center; justify-content: center; font-family: "Lora", serif; font-style: italic; font-size: 16px; color: var(--black); }

  .terms-label { background: var(--orange); color: var(--black); font-weight: 700; font-size: 9px; padding: 1px 4px; }
  .terms-text { font-size: 9px; font-weight: 700; line-height: 15px; }
  .rule { height: 1px; background: var(--silver); }

  /* Colour bar side */
  .colour-copy { font-size: 10.5px; font-weight: 700; line-height: 17px; }
  .wine-note { font-size: 12px; font-weight: 700; line-height: 19px; text-align: center; }
  .contact-band { left: 0; top: 333px; width: 470px; height: 234px; background: var(--orange); }
  .brand-panel { left: 75px; top: 15px; width: 305px; height: 58px; background: #fff; border-radius: 10px; box-shadow: 0 0 0 3px #fff, 0 0 0 5px #e06820; display: flex; flex-direction: column; align-items: center; justify-content: center; }
  .brand-panel .brand-name { font-size: 32px; }
  .brand-panel .brand-tagline { font-size: 8.5px; margin-top: 2px; }
  .locate-pill { left: 75px; top: 90px; background: #fff; color: var(--orange); font-weight: 900; font-size: 12px; padding: 2px 8px; border-radius: 10px; }
  .contact-list { left: 28px; top: 122px; list-style: none; font-size: 10.5px; font-weight: 700; color: #fff; line-height: 20px; }
  .contact-list li { display: flex; align-items: flex-start; gap: 7px; }
  .contact-list svg { width: 10px; height: 10px; margin-top: 5px; flex: none; }
  .map-frame { left: 238px; top: 92px; width: 210px; height: 130px; border: 3px solid #fff; border-radius: 10px; background: linear-gradient(135deg,#e4e1dc,#cfccc6); }
</style>
</head>
<body>

<section class="flyer-side side-men">
  <div class="abs brand-name" style="left:55px;top:24px;">velquora</div>
  <div class="abs brand-tagline" style="left:58px;top:64px;">HAIR, SKIN AND GROOMING STUDIO</div>
  <p class="abs intro" style="left:35px;top:86px;width:405px;">Velquora is appreciation of all things beautiful. We believe that beauty is etched in our personalities. We strive to create positive experiences. To enhance individual style with superior grooming. To celebrate diversity and all things feminine.</p>

  <div class="abs power-band">
    <div class="abs power-box">
      <div class="abs power-title">A MALE "POWER HOUR"</div>
      <div class="abs power-sub">(75mins of serious grooming)<br>with <strong>BRENNA</strong></div>
      <div class="abs power-line">Choose any 2 male treatments from the following menus for just $99!</div>
    </div>
    <div class="abs power-photo" role="img" aria-label="Portrait photo of Brenna, the male grooming therapist"></div>
  </div>

  <div class="abs offer-tag">
    <div class="abs tag-back"></div>
    <div class="abs tag-front">Offer 1</div>
  </div>

  <div class="abs photo-frame" style="left:310px;top:220px;width:118px;height:104px;">
    <div class="photo-fill" role="img" aria-label="Photo of a man receiving a back massage" style="background:linear-gradient(135deg,#6b4a36,#c9a088);"></div>
  </div>
  <span class="abs section-label" style="right:163px;top:236px;">BODY</span>
  <ul class="abs menu-list align-right" style="right:163px;top:254px;">
    <li>30 minute deep tissue massage</li>
    <li>Full body detox body scrub</li>
    <li>Mens maintenance pedicure</li>
    <li>Mens maintenance manicure</li>
  </ul>

  <div class="abs photo-frame" style="left:28px;top:345px;width:118px;height:106px;">
    <div class="photo-fill" role="img" aria-label="Photo of a young man touching his hair" style="background:linear-gradient(135deg,#f4f4f4,#d9b8a0);"></div>
  </div>
  <span class="abs section-label" style="left:152px;top:371px;">FACE</span>
  <ul class="abs menu-list" style="left:153px;top:389px;">
    <li>Express Deep Cleanse Facial</li>
    <li>Microdermabrasion</li>
    <li>30 minute Indian head massage</li>
  </ul>

  <div class="abs photo-frame" style="left:310px;top:475px;width:118px;height:106px;">
    <div class="photo-fill" role="img" aria-label="Photo of a man's bare back and shoulders" style="background:linear-gradient(135deg,#f2f2f2,#7a5440);"></div>
  </div>
  <span class="abs section-label" style="right:163px;top:490px;">MANSCAPING</span>
  <ul class="abs menu-list align-right" style="right:163px;top:508px;">
    <li>Back and shoulder wax</li>
    <li>Chest and Stomach</li>
    <li>Mens Basic bikini (speedo line)</li>
    <li>1/2 leg wax</li>
  </ul>

  <span class="abs terms-label" style="left:33px;top:584px;">TERMS &amp; CONDITIONS</span>
  <p class="abs terms-text" style="left:33px;top:600px;width:350px;">Offered by appointment with Brenna our Male grooming therapist only various days &amp; times subject to availability, subject to change without notice; limitless services per customer</p>
  <div class="abs rule" style="left:33px;top:645px;width:385px;"></div>
</section>

<section class="flyer-side side-colour">
  <p class="abs intro" style="left:38px;top:28px;width:400px;">Velquora is appreciation of all things beautiful. We believe that beauty is etched in our personalities. We strive to create positive experiences. To enhance individual style with superior grooming. To celebrate diversity and all things feminine.</p>

  <span class="abs section-label" style="left:33px;top:121px;">MARLOWS "COLOUR BAR"</span>
  <div class="abs colour-copy" style="left:34px;top:138px;width:210px;">
    (available Tues - Thurs) $99<br>
    Freshen up your look in the experienced hands of a Senior Stylist<br>
    1/2 head of foils or regrowth colour<br>
    Precision style cut and Blowdry
  </div>
  <p class="abs wine-note" style="left:20px;top:258px;width:215px;">Appointments after 4pm -<br>Enjoy a complimentry glass of wine</p>

  <div class="abs photo-frame" style="left:270px;top:100px;width:164px;height:218px;">
    <div class="photo-fill" role="img" aria-label="Portrait photo of Marlow, the senior stylist" style="background:linear-gradient(160deg,#7a5a3e,#b89270 55%,#3a3140);"></div>
  </div>

  <div class="abs contact-band">
    <div class="abs brand-panel">
      <div class="brand-name">velquora</div>
      <div class="brand-tagline">HAIR, SKIN AND GROOMING STUDIO</div>
    </div>
    <span class="abs locate-pill">LOCATE US</span>
    <ul class="abs contact-list">
      <li><svg viewBox="0 0 10 10"><path d="M2 1 L4 1 L4.6 3 L3.4 4 Q4.4 5.8 6 6.6 L7 5.4 L9 6 L9 8 Q5 9 1.5 4.5 Q1 2.5 2 1Z" fill="#111"/></svg>+61 7 3000 4827</li>
      <li><svg viewBox="0 0 10 10"><rect x="0.5" y="2" width="9" height="6.5" fill="#111"/><path d="M0.5 2 L5 5.5 L9.5 2" stroke="#f47c30" stroke-width="0.9" fill="none"/></svg>info@velquorastudio.net.au</li>
      <li><svg viewBox="0 0 10 10"><circle cx="5" cy="5" r="4.3" fill="none" stroke="#111" stroke-width="1.2"/><ellipse cx="5" cy="5" rx="1.8" ry="4.3" fill="none" stroke="#111" stroke-width="0.9"/><path d="M0.7 5 H9.3" stroke="#111" stroke-width="0.9"/></svg>www.velquorastudio.net.au</li>
      <li><svg viewBox="0 0 10 10"><path d="M5 0.8 L9.5 5 L8 5 L8 9 L6 9 L6 6.5 L4 6.5 L4 9 L2 9 L2 5 L0.5 5Z" fill="#111"/></svg><span>12 / 240 Marrow Street, Elmvale<br>Brisbane, Queensland, Australia 4000</span></li>
    </ul>
    <div class="abs map-frame" role="img" aria-label="Street map showing the salon location"></div>
  </div>

  <span class="abs terms-label" style="left:181px;top:580px;">TERMS &amp; CONDITIONS</span>
  <p class="abs terms-text" style="left:55px;top:600px;">AVAILABLE FOR LIMITED TIMES</p>
  <p class="abs terms-text" style="left:243px;top:598px;">16th Sept - 6th Nov 2014 &amp; 30th Dec - 27th Feb</p>
  <p class="abs terms-text" style="left:0;width:470px;text-align:center;top:619px;">With Marlow only &amp; for one service per customer at advertised price of $99</p>
  <div class="abs rule" style="left:33px;top:645px;width:385px;"></div>
</section>

</body>
</html>
```